Upscale dog care facility need some marketing material

We offer a lot of services for dogs and their humans. We have a large indoor dog park, swimming pools, dog daycare and boarding, Pet CPR/First Aid classes and training. We love the trifold brochures where we can highlight all of our services (even a few pics of the facility) as well as give everyone information on our pricing and membership concepts. Will primarily be used for marketing to vets and local pet stores to help get the word out about our business.

```html
<!DOCTYPE html>
<html lang="en">
<head>
<meta charset="utf-8">
<title>Splash &amp; Sniff – Brochure Outside</title>
<link href="https://fonts.googleapis.com/css2?family=Oswald:wght@500;700&family=Open+Sans:wght@400;600;700&display=swap" rel="stylesheet">
<style>
  :root{
    --bg:#e6e9ed;
    --paper:#ffffff;
    --blue:#1b9ad6;
    --blue-light:#6cc7ef;
    --navy:#0e3468;
    --ink:#4a5460;
    --pale:#eaf6fc;
  }
  *{box-sizing:border-box;margin:0;padding:0}
  html,body{width:800px;height:1200px;overflow:hidden;background:var(--bg)}
  body{font-family:"Open Sans",sans-serif;color:var(--ink);position:relative}
  .brochure{position:absolute;left:10px;top:405px;width:780px;height:390px;background:var(--paper);
    box-shadow:0 6px 22px rgba(0,0,0,.18);display:flex;overflow:hidden}
  .panel{position:relative;width:260px;height:100%;overflow:hidden}
  .panel + .panel{border-left:1px solid #eef1f4}
  .wave{position:absolute;left:0;width:100%}
  .wave.top{top:0}
  .wave.bottom{bottom:0}
  .footer-text{position:absolute;bottom:6px;left:0;width:100%;text-align:center;color:#fff;font-size:6.5px;font-weight:600;letter-spacing:.3px}
  .heading{display:flex;align-items:center;gap:6px;font-family:"Oswald",sans-serif;font-weight:700;color:var(--navy);font-size:15px;letter-spacing:.5px}
  .heading .dot{width:14px;height:14px;border-radius:50%;background:var(--blue)}
  .body-text{font-size:6px;line-height:1.55;color:var(--ink)}
  .photo{position:absolute;background:radial-gradient(circle at 45% 40%,#f3e6cc 0 22%,#7fcbee 45%,#2a9bd6 100%)}

  /* left panel */
  .who .heading{position:absolute;left:20px;top:42px}
  .who .intro{position:absolute;left:20px;top:66px;width:222px}
  .who .services{position:absolute;left:20px;top:140px;font-family:"Oswald",sans-serif;font-weight:700;color:var(--blue);font-size:17px;line-height:1.1}
  .who .photo{left:28px;top:196px;width:108px;height:108px;border-radius:50%;border:4px solid var(--blue-light);
    background:radial-gradient(circle at 50% 45%,#f4ead6 0 25%,#9fd47a 55%,#4f9b3f 100%)}
  .who .note{position:absolute;left:146px;top:212px;width:100px}

  /* middle panel */
  .visit .heading{position:absolute;left:60px;top:40px}
  .visit .intro{position:absolute;left:22px;top:64px;width:218px}
  .visit .quote{position:absolute;left:22px;top:140px;width:216px;padding:9px 10px 9px;border:1px solid #cfe7f4;background:var(--pale);border-radius:6px;text-align:center}
  .visit .photo{left:88px;top:196px;width:84px;height:84px;border-radius:50%;border:3px solid #fff;box-shadow:0 0 0 2px var(--blue)}
  .visit .client{position:absolute;left:0;top:284px;width:100%;text-align:center;font-size:7px;font-weight:700;color:var(--navy)}
  .visit .contact{position:absolute;left:22px;top:302px}
  .visit .contact h3{font-family:"Oswald",sans-serif;font-size:10px;color:var(--blue);margin-bottom:4px}
  .contact-row{display:flex;align-items:center;gap:5px;font-size:6px;margin-bottom:3px}
  .contact-row svg{width:8px;height:8px;flex:none}

  /* right panel */
  .cover .brand{position:absolute;right:20px;top:26px;display:flex;align-items:center;gap:5px;font-family:"Oswald",sans-serif;font-weight:700;color:var(--navy);font-size:15px}
  .cover .brand .mark{width:10px;height:10px;border-radius:50%;background:var(--blue)}
  .cover .photo{left:0;top:62px;width:260px;height:150px;
    background:radial-gradient(ellipse at 40% 45%,#f3e4c2 0 18%,#5fc0ec 42%,#1579b8 100%);
    clip-path:path('M0 0 H260 V150 C180 120 90 160 0 130 Z')}
  .cover .arc{position:absolute;left:0;top:62px}
  .cover .welcome{position:absolute;right:20px;top:226px;font-size:7px;font-weight:700;color:var(--navy);letter-spacing:.6px;text-align:right}
  .cover .title{position:absolute;right:20px;top:236px;font-family:"Oswald",sans-serif;font-weight:700;color:var(--blue);font-size:28px;letter-spacing:.5px;text-align:right}
  .cover .intro{position:absolute;right:20px;top:282px;width:210px;text-align:right}
</style>
</head>
<body>
<main class="brochure">

  <section class="panel who">
    <svg class="wave top" viewBox="0 0 260 34" height="34" preserveAspectRatio="none"><path d="M0 0H260V14C190 30 110 4 0 26Z" fill="var(--blue)"/><path d="M0 26C110 4 190 30 260 14V20C190 36 110 10 0 32Z" fill="var(--blue-light)"/></svg>
    <h2 class="heading"><span class="dot"></span>WHO WE ARE</h2>
    <p class="body-text intro">Splash &amp; Sniff, located in Brookfield, is a new and unique dog facility that focuses on building and supporting relationships between dogs and their families. We encourage our members to bring in a swimsuit, play, and swim with their dogs. We offer the most indoor play space in the area, warm heated pools, and friendly staff trained in pet first aid.</p>
    <h3 class="services">DAYCARE,<br>ROOM RENTAL,<br>CLASSES AND MORE!</h3>
    <div class="photo" role="img" aria-label="Photo of a dog playing on grass"></div>
    <p class="body-text note">Splash &amp; Sniff offers day visits, boarding, private pool time and CPR classes so every dog and owner feels welcome here.</p>
    <svg class="wave bottom" viewBox="0 0 260 30" height="30" preserveAspectRatio="none"><path d="M0 10C90 -4 170 18 260 4V30H0Z" fill="var(--blue)"/></svg>
    <p class="footer-text">hello@splashandsniff.example</p>
  </section>

  <section class="panel visit">
    <svg class="wave top" viewBox="0 0 260 34" height="34" preserveAspectRatio="none"><path d="M0 0H260V22C170 6 90 30 0 12Z" fill="var(--blue)"/><path d="M0 12C90 30 170 6 260 22V28C170 12 90 36 0 18Z" fill="var(--blue-light)"/></svg>
    <h2 class="heading"><span class="dot"></span>BEFORE YOU VISIT?</h2>
    <p class="body-text intro">Splash &amp; Sniff offers a range of memberships, passes, single visits, room rentals and classes. To keep our animals healthy, all dogs must show current vaccine records before entry. Bring a towel, a leash, and a happy pup, and our team will guide you through a short first visit tour.</p>
    <div class="quote body-text">"We love our weekly swim here. The staff are kind, the pools are clean, and our dog sleeps soundly every night after a visit. Highly recommended!"</div>
    <div class="photo" role="img" aria-label="Photo of a dog wearing swim goggles"></div>
    <p class="client">Client Name</p>
    <div class="contact">
      <h3>Get in Touch</h3>
      <div class="contact-row"><svg viewBox="0 0 10 10"><path d="M2 1l2 2-1 1.5a6 6 0 0 0 2.5 2.5L7 6l2 2-1.5 1.5C4 9 1 6 .5 2Z" fill="var(--blue)"/></svg>(555) 014-2290</div>
      <div class="contact-row"><svg viewBox="0 0 10 10"><path d="M5 0a3.5 3.5 0 0 0-3.5 3.5C1.5 6 5 10 5 10s3.5-4 3.5-6.5A3.5 3.5 0 0 0 5 0Zm0 5a1.5 1.5 0 1 1 0-3 1.5 1.5 0 0 1 0 3Z" fill="var(--blue)"/></svg>120 Harbor Lane, Brookfield</div>
      <div class="contact-row"><svg viewBox="0 0 10 10"><rect x=".5" y="2" width="9" height="6" rx="1" fill="none" stroke="var(--blue)"/><path d="M.5 2.5L5 6l4.5-3.5" fill="none" stroke="var(--blue)"/></svg>hello@splashandsniff.example</div>
    </div>
    <svg class="wave bottom" viewBox="0 0 260 30" height="30" preserveAspectRatio="none"><path d="M0 6C80 18 180 -2 260 10V30H0Z" fill="var(--blue)"/></svg>
    <p class="footer-text">splashandsniff.example</p>
  </section>

  <section class="panel cover">
    <svg class="wave top" viewBox="0 0 260 20" height="20" preserveAspectRatio="none"><path d="M0 0H260V8C170 18 90 2 0 12Z" fill="var(--blue)"/></svg>
    <div class="brand"><span class="mark"></span>Splash &amp; Sniff</div>
    <div class="photo" role="img" aria-label="Photo of a dog swimming in a blue pool"></div>
    <svg class="arc" width="260" height="160" viewBox="0 0 260 160"><path d="M0 130C90 160 180 120 260 150" fill="none" stroke="var(--blue)" stroke-width="5"/><path d="M0 138C90 168 180 128 260 158" fill="none" stroke="var(--blue-light)" stroke-width="2"/></svg>
    <p class="welcome">WELCOME TO SPLASH &amp; SNIFF</p>
    <h1 class="title">POOL, PARK, FUN</h1>
    <p class="body-text intro">Splash &amp; Sniff is a place for dogs and their humans to enjoy time together in a safe, clean and comfortable environment with indoor play, warm pools and caring staff.</p>
    <svg class="wave bottom" viewBox="0 0 260 30" height="30" preserveAspectRatio="none"><path d="M0 12C90 0 170 20 260 6V30H0Z" fill="var(--blue)"/></svg>
    <p class="footer-text">Call: (555) 014-2290</p>
  </section>

</main>
</body>
</html>
```